THE POINT AT MAPLE SWALE HUDSON RIVER WATERFRONT LAND

crisp clear business cards on wood stock or thick paper with large font with a river otter logo, PERSONAL INFO ON ONE SIDE, PROJECT INFO ON THE OTHER SIDE
Updates

I don’t have a logo. Just thought that a photo of a river otter would look appealing.

Target Market(s)

Buyers and realtors

Industry/Entity Type

Real Estate Development

Contact Information for Business Card

MARTIN OSGOOD
518-730-4862 (Call or Text)
STONE HAVEN LLC PRINCIPAL

MOSHAVENRD@TARNMAIL.COM

Font styles to use
Sans Serif

Colors
fbfdfe
0792cd
00a990
fbed22
ec1f27

Requirements
Must have
• LARGE FONT, ROUNDED EDGES,
Nice to have
• ON THE BACK SIDE :
• THE POINT AT MAPLE SWALE
• HUDSON RIVER WATERFRONT LAND
• 2 TO 67 ACRES---READY TO BUILD
• PRICED TO SELL!

```html
<!DOCTYPE html>
<html lang="en">
<head>
<meta charset="utf-8">
<title>Stone Haven LLC — Business Card</title>
<link rel="stylesheet" href="https://fonts.googleapis.com/css2?family=Work+Sans:wght@400;500;600&display=swap">
<style>
  :root {
    --bg-top: #2a2a2a;
    --bg-bottom: #141414;
    --card: #242424;
    --card-shade: #1c1c1c;
    --blue: #0792cd;
    --paper-white: #fbfdfe;
  }
  * { box-sizing: border-box; margin: 0; padding: 0; }
  html, body { width: 1200px; height: 900px; overflow: hidden; }
  body {
    background: radial-gradient(ellipse at 50% 30%, var(--bg-top), var(--bg-bottom) 75%);
    font-family: "Work Sans", Arial, sans-serif;
    color: var(--paper-white);
    display: flex;
    flex-direction: column;
    align-items: center;
    justify-content: center;
    gap: 24px;
  }
  .card {
    position: relative;
    width: 700px;
    height: 400px;
    background: linear-gradient(135deg, var(--card-shade), var(--card) 60%, #2c2c2c);
    border-radius: 6px;
    overflow: hidden;
    box-shadow: 0 14px 30px rgba(0,0,0,0.55);
  }
  .card::after {
    content: "";
    position: absolute;
    left: 0; right: 0; bottom: 0;
    height: 6px;
    background: var(--blue);
  }

  /* Project side */
  .company-name {
    position: absolute;
    top: 150px;
    left: 0; right: 0;
    text-align: center;
    font-weight: 600;
    font-size: 46px;
    letter-spacing: 4px;
    color: var(--blue);
  }
  .project-lines {
    position: absolute;
    bottom: 40px;
    left: 0; right: 0;
    text-align: center;
    font-size: 16px;
    font-weight: 500;
    letter-spacing: 1px;
    line-height: 1.6;
    text-transform: uppercase;
  }

  /* Personal side */
  .identity {
    position: absolute;
    top: 150px;
    right: 400px;
    text-align: right;
  }
  .person-name {
    font-size: 34px;
    font-weight: 600;
    color: var(--blue);
    letter-spacing: 0.5px;
    white-space: nowrap;
  }
  .person-role { font-size: 21px; font-weight: 400; }
  .divider {
    position: absolute;
    top: 160px;
    left: 318px;
    width: 2px;
    height: 70px;
    background: var(--blue);
  }
  .contact {
    position: absolute;
    top: 165px;
    left: 340px;
    list-style: none;
    font-size: 19px;
    line-height: 1.55;
  }
  .contact li { display: flex; align-items: center; gap: 10px; white-space: nowrap; }
  .contact svg { width: 14px; height: 14px; flex: none; }
  .address {
    position: absolute;
    bottom: 40px;
    left: 0; right: 0;
    text-align: center;
    font-size: 21px;
    letter-spacing: 0.5px;
  }
</style>
</head>
<body>
  <section class="card card-project">
    <h1 class="company-name">STONE HAVEN LLC</h1>
    <p class="project-lines">
      The Point at Maple Swale | Hudson River Waterfront Land<br>
      2 to 67 Acres---Ready to Build &nbsp;| Priced to Sell!
    </p>
  </section>

  <section class="card card-personal">
    <div class="identity">
      <h2 class="person-name">MARTIN OSGOOD</h2>
      <p class="person-role">Principal</p>
    </div>
    <span class="divider"></span>
    <ul class="contact">
      <li>
        <svg viewBox="0 0 24 24" aria-hidden="true"><path fill="#0792cd" d="M6.6 10.8a15.1 15.1 0 0 0 6.6 6.6l2.2-2.2a1 1 0 0 1 1-.25 11.4 11.4 0 0 0 3.6.57 1 1 0 0 1 1 1V20a1 1 0 0 1-1 1A17 17 0 0 1 3 4a1 1 0 0 1 1-1h3.5a1 1 0 0 1 1 1c0 1.25.2 2.45.57 3.57a1 1 0 0 1-.25 1z"/></svg>
        518-730-4862
      </li>
      <li>
        <svg viewBox="0 0 24 24" aria-hidden="true"><rect x="3" y="5" width="18" height="14" rx="1.5" fill="none" stroke="#0792cd" stroke-width="2"/><path d="M3 6l9 7 9-7" fill="none" stroke="#0792cd" stroke-width="2"/></svg>
        moshavenrd@tarnmail.com
      </li>
    </ul>
    <p class="address">412b Harlow Lane, Ashford, NZ, 8024</p>
  </section>
</body>
</html>
```